*** Business Card Design Project

As a starting point, please take a look at our website www.plentarohire.com as a starting point.

We are looking for you to design our new business cards for plentarohire, something funky, cool and potentially unusual/different.

Good luck.

Industry/Entity Type

Business

```html
<!DOCTYPE html>
<html lang="en">
<head>
<meta charset="utf-8">
<title>Plentaro Hire – Business Cards</title>
<link href="https://fonts.googleapis.com/css2?family=Source+Sans+3:wght@400;700&display=swap" rel="stylesheet">
<style>
  :root {
    --page: #ffffff;
    --card: #000000;
    --white: #ffffff;
    --cyan: #33c6d8;
    --green: #8fd63a;
    --plum: #a6377f;
    --magenta: #d3238a;
  }
  * { margin: 0; padding: 0; box-sizing: border-box; }
  html, body {
    width: 1200px; height: 775px; overflow: hidden;
    background: var(--page);
    font-family: "Source Sans 3", "Myriad Pro", Arial, sans-serif;
  }
  .sheet { position: relative; width: 1200px; height: 775px; }
  .card {
    position: absolute;
    width: 549px; height: 300px;
    background: var(--card);
    border-radius: 9px;
    overflow: hidden;
  }
  .card--front-a { left: 27px;  top: 41px; }
  .card--back-a  { left: 625px; top: 41px; }
  .card--front-b { left: 27px;  top: 423px; }
  .card--back-b  { left: 625px; top: 423px; }

  .sliver { position: absolute; left: 76px; top: 0; width: 8px; height: 300px; }

  .side-text {
    position: absolute; top: 14px;
    writing-mode: vertical-rl;
    white-space: nowrap;
    line-height: 1;
  }
  .side-text--address { left: 20px; font-size: 15px; }
  .side-text--phone   { left: 42px; font-size: 15px; }
  .side-text--email   { left: 30px; font-size: 20px; }
  .card--front-a .side-text { color: var(--plum); }
  .card--front-b .side-text { color: var(--magenta); }
  .card--back-a .side-text  { color: var(--green); }
  .card--back-b .side-text  { color: var(--cyan); }

  .wordmark {
    position: absolute; left: 236px; top: 58px;
    font-size: 54px; font-weight: 400; line-height: 74px;
  }
  .card--front-a .wordmark { color: var(--cyan); }
  .card--front-b .wordmark { color: var(--white); }

  .contact {
    position: absolute; left: 84px; right: 0; top: 62px;
    text-align: center; color: var(--white);
  }
  .contact__name  { font-size: 25px; font-weight: 700; line-height: 32px; }
  .contact__title { font-size: 25px; font-weight: 400; line-height: 32px; text-transform: uppercase; }
  .contact__phones { margin-top: 58px; font-size: 19px; line-height: 29px; }
  .card--back-a .contact__phones { color: var(--green); }
  .card--back-b .contact__phones { color: var(--cyan); }
</style>
</head>
<body>
<main class="sheet">

  <section class="card card--front-a">
    <p class="side-text side-text--address">42-44 Larkfield Row London EC2M 7RT</p>
    <p class="side-text side-text--phone">+44 203 555 0190</p>
    <svg class="sliver" viewBox="0 0 8 300" aria-hidden="true"><path d="M4 0 Q7.5 150 4 300 Q0.5 150 4 0Z" fill="#fff"/></svg>
    <h1 class="wordmark">Plentaro<br>Hire</h1>
  </section>

  <section class="card card--back-a">
    <p class="side-text side-text--email">marcus@plentarohire.com</p>
    <svg class="sliver" viewBox="0 0 8 300" aria-hidden="true"><path d="M4 0 Q7.5 150 4 300 Q0.5 150 4 0Z" fill="#fff"/></svg>
    <div class="contact">
      <p class="contact__name">Marcus Ellery</p>
      <p class="contact__title">Managing Director</p>
      <p class="contact__phones">(+44) 0203 555 0148<br>(+44) 07700 900412</p>
    </div>
  </section>

  <section class="card card--front-b">
    <p class="side-text side-text--address">42-44 Larkfield Row London EC2M 7RT</p>
    <p class="side-text side-text--phone">+44 203 555 0190</p>
    <svg class="sliver" viewBox="0 0 8 300" aria-hidden="true"><path d="M4 0 Q7.5 150 4 300 Q0.5 150 4 0Z" fill="#fff"/></svg>
    <h1 class="wordmark">Plentaro<br>Hire</h1>
  </section>

  <section class="card card--back-b">
    <p class="side-text side-text--email">marcus@plentarohire.com</p>
    <svg class="sliver" viewBox="0 0 8 300" aria-hidden="true"><path d="M4 0 Q7.5 150 4 300 Q0.5 150 4 0Z" fill="#fff"/></svg>
    <div class="contact">
      <p class="contact__name">Simon Hartwell</p>
      <p class="contact__title">Account Director</p>
      <p class="contact__phones">(+44) 0203 555 0146<br>(+44) 07700 900857</p>
    </div>
  </section>

</main>
</body>
</html>
```